Bref créative
Martin L. Hollis
Attorney & Counselor at Law
I need double sided standard sized Business Card [3.5" x 2"]
Use different font, but that coordinates with the logo font. I am open to different variations.
Simple
20847 52nd Ave Ct SW, Ste 214
Lakewood, WA 98512
martin@martinlhollis.com
http://www.martinlhollis.com
The logo that should be used on the card should be the second version that I had the artist prepare.
Add my email address on the front of the card.
Email Address: martin@martinlhollis.com
[Insert business logo at top]
[Smaller font] Established 1982
[Larger font with bullet each line]
Divorce & Family Law
Domestic Violence
DUI & Other Criminal Defense
Bankruptcy
I have been requested to upload the *.ai file. Here it is.
This is the *.ai file for the alternate design. This is a variation on the first design. I would like to see what each one looks like on the business card. This design will save space on the card because the logo is on the same line as the text.

```html
<!DOCTYPE html>
<html lang="en">
<head>
<meta charset="utf-8">
<title>Martin L. Hollis – Stationery</title>
<link href="https://fonts.googleapis.com/css2?family=Arimo:wght@400;700&family=Tinos:ital@1&display=swap" rel="stylesheet">
<style>
  :root {
    --backdrop: #2b1b17;
    --paper: #ffffff;
    --navy: #1f3158;
    --navy-deep: #172647;
    --ink: #1c2b4d;
    --text-dark: #333333;
    --rule-grey: #6a6a6a;
    --edge-grey: #e4e4e4;
    --watermark: #e9eaec;
    --watermark-navy: #2a3d66;
    --on-navy: #ffffff;
  }
  * { margin: 0; padding: 0; box-sizing: border-box; }
  html, body { width: 1200px; height: 901px; overflow: hidden; }
  body {
    background: var(--backdrop);
    font-family: "Arimo", Arial, sans-serif;
    color: var(--text-dark);
    position: relative;
  }
  .sheet { position: absolute; background: var(--paper); overflow: hidden; }

  /* Brand lockup: plain square + name */
  .brand { text-align: center; color: var(--ink); }
  .brand-mark { display: block; margin: 0 auto 4px; background: var(--ink); }
  .brand-name { font-weight: 400; letter-spacing: 0.3px; line-height: 1.1; }
  .brand-tag { margin-top: 2px; color: var(--ink); }

  .watermark {
    position: absolute;
    background: linear-gradient(180deg, var(--watermark), #f3f4f5);
  }

  /* Letterhead */
  .letterhead { left: 214px; top: 44px; width: 528px; height: 820px; z-index: 1; }
  .letterhead .brand { position: absolute; left: 0; right: 0; top: 8px; }
  .letterhead .brand-mark { width: 30px; height: 30px; }
  .letterhead .brand-name { font-size: 15px; }
  .letterhead .brand-tag { font-size: 6px; }
  .letterhead .watermark { left: 66px; top: 175px; width: 365px; height: 475px; }
  .letterhead-footer {
    position: absolute; left: 0; right: 0; top: 742px; height: 70px;
    background: var(--navy); color: var(--on-navy);
    font-size: 8.5px; text-align: center; line-height: 13px; padding-top: 14px;
  }
  .letterhead-edge { position: absolute; left: 0; right: 0; bottom: 0; height: 8px; background: var(--edge-grey); }

  /* Business card back (navy) */
  .card-back {
    left: 78px; top: 146px; width: 324px; height: 170px; z-index: 2;
    background: var(--navy); color: var(--on-navy);
  }
  .card-back .watermark {
    left: 8px; top: 12px; width: 110px; height: 150px;
    background: var(--watermark-navy);
  }
  .card-back .services {
    position: absolute; left: 70px; right: 10px; top: 28px;
    text-align: center; font-size: 10px; line-height: 12.5px;
  }
  .card-back .motto { margin-bottom: 12px; }

  /* Business card front */
  .card-front { left: 718px; top: 85px; width: 370px; height: 202px; z-index: 2; }
  .card-front .holder { position: absolute; right: 14px; top: 10px; font-size: 11px; }
  .card-front .brand { position: absolute; left: 110px; top: 28px; width: 220px; }
  .card-front .brand-mark { width: 30px; height: 30px; }
  .card-front .brand-name { font-size: 18px; }
  .card-front .brand-tag { font-size: 6.5px; }
  .card-front .contact {
    position: absolute; left: 0; right: 0; top: 142px;
    text-align: center; font-size: 8.5px; line-height: 11px; color: var(--text-dark);
  }
  .card-front .base { position: absolute; left: 0; right: 0; bottom: 0; height: 12px; background: var(--rule-grey); }

  /* Compliment slip */
  .slip { left: 555px; top: 377px; width: 516px; height: 292px; z-index: 3; }
  .slip .brand { position: absolute; left: 8px; top: 10px; width: 120px; }
  .slip .brand-mark { width: 24px; height: 24px; }
  .slip .brand-name { font-size: 13px; }
  .slip .brand-tag { font-size: 5.5px; }
  .slip .watermark { left: 333px; top: 25px; width: 134px; height: 170px; }
  .slip .greeting {
    position: absolute; right: 166px; top: 196px;
    font-family: "Tinos", "Times New Roman", serif; font-style: italic;
    font-size: 12px; color: var(--text-dark);
  }
  .slip-footer {
    position: absolute; left: 0; right: 0; top: 217px; height: 48px;
    background: var(--navy-deep); color: var(--on-navy);
    font-size: 7px; line-height: 10px; text-align: center; padding-top: 8px;
  }
  .slip-edge { position: absolute; left: 0; right: 0; bottom: 0; height: 27px; background: var(--edge-grey); }
</style>
</head>
<body>

  <section class="sheet letterhead">
    <div class="watermark" role="img" aria-label="Faint monogram watermark area"></div>
    <div class="brand">
      <span class="brand-mark"></span>
      <div class="brand-name">Martin L. Hollis</div>
      <div class="brand-tag">Attorney &amp; Counselor at Law</div>
    </div>
    <footer class="letterhead-footer">
      <div>20847 52nd Ave Ct SW, Ste 214, Lakewood, WA 98512</div>
      <div>License No: WSBA 40217</div>
      <div>Phone : 253 412-0375 &nbsp;Fax : 253 412-0376 &nbsp;Email : martin@martinlhollis.com &nbsp;http://www.martinlhollis.com</div>
    </footer>
    <div class="letterhead-edge"></div>
  </section>

  <section class="sheet card-back">
    <div class="watermark" role="img" aria-label="Faint monogram watermark area"></div>
    <div class="services">
      <p class="motto">"our Family Helping Yours"</p>
      <p>Divorce &amp; Family Law</p>
      <p>Domestic Violence</p>
      <p>DUI &amp; Other Criminal Defense</p>
      <p>Bankruptcy</p>
    </div>
  </section>

  <section class="sheet card-front">
    <div class="holder">Martin L. Hollis</div>
    <div class="brand">
      <span class="brand-mark"></span>
      <div class="brand-name">Martin L. Hollis</div>
      <div class="brand-tag">Attorney &amp; Counselor at Law</div>
    </div>
    <div class="contact">
      <div>20847 52nd Ave Ct SW, Ste 214, Lakewood, WA 98512</div>
      <div>Phone : 253 412-0375 &nbsp;&nbsp;Fax : 253 412-0376</div>
      <div>Email : martin@martinlhollis.com &nbsp;&nbsp;http://www.martinlhollis.com</div>
    </div>
    <div class="base"></div>
  </section>

  <section class="sheet slip">
    <div class="watermark" role="img" aria-label="Faint monogram watermark area"></div>
    <div class="brand">
      <span class="brand-mark"></span>
      <div class="brand-name">Martin L. Hollis</div>
      <div class="brand-tag">Attorney &amp; Counselor at Law</div>
    </div>
    <p class="greeting">With Compliments</p>
    <footer class="slip-footer">
      <div>20847 52nd Ave Ct SW, Ste 214, Lakewood, WA 98512</div>
      <div>License No: WSBA 40217</div>
      <div>Phone : 253 412-0375 &nbsp;Fax : 253 412-0376 &nbsp;Email : martin@martinlhollis.com &nbsp;http://www.martinlhollis.com</div>
    </footer>
    <div class="slip-edge"></div>
  </section>

</body>
</html>
```